Velvet Harbor Powerpoint Presentation

Looking for powerpoint presentation template for our boutique social media management and digital marketing company.
We will be using this Powerpoint template for presentations, guest speaking sessions and proposals.
We need a front page and then a few different versions of what the rest of the template would look like.
I have attached our business cards, different versions of our logo, and our PDF so you can get a look at our identity and get a feel of what we are about. Our website will be up in about two weeks.
Target Market(s)
Small to medium size business owners (all different catagories)
Industry/Entity Type
Marketing
Requirements
Must have
- The logo
- a very boutique, high end look. You will see what I mean when you look at our business cards and our PDF.
- We only want to use the Velvet Harbor colors- Black, White, Rose Gold and Grey
Should not have
- Lot's of colors that are not part of the Velvet Harbor identity

```html
<!DOCTYPE html>
<html lang="en">
<head>
<meta charset="utf-8">
<title>Velvet Harbor Presentation Template</title>
<link href="https://fonts.googleapis.com/css2?family=Montserrat:wght@400;600&family=Open+Sans:wght@400;600&display=swap" rel="stylesheet">
<style>
  :root {
    --backdrop: #9b9b9b;
    --rose: #e8845f;
    --rose-soft: #f3b79f;
    --charcoal: #3f3f41;
    --grey: #707072;
    --grey-light: #e4e4e4;
    --paper: #ffffff;
    --ink: #5a5a5a;
  }
  * { box-sizing: border-box; margin: 0; padding: 0; }
  html, body { width: 867px; height: 1200px; overflow: hidden; }
  body {
    background: var(--backdrop);
    position: relative;
    font-family: "Open Sans", Arial, sans-serif;
    color: var(--ink);
  }
  .slide {
    position: absolute;
    width: 310px; height: 217px;
    background: var(--paper);
    overflow: hidden;
    box-shadow: 0 2px 6px rgba(0,0,0,.25);
  }
  .col-left { left: 116px; } .col-right { left: 448px; }
  .row-1 { top: 101px; } .row-2 { top: 355px; } .row-3 { top: 613px; } .row-4 { top: 867px; }
  .abs { position: absolute; }
  .photo { position: absolute; }
  .slide-title {
    position: absolute; top: 14px; left: 0; right: 0;
    font-family: "Montserrat", Arial, sans-serif;
    font-size: 8px; letter-spacing: 1px; color: var(--rose);
    text-align: center; text-transform: uppercase;
  }
  .slide-title.left { left: 16px; text-align: left; }
  .body-text { font-size: 4.8px; line-height: 1.6; color: var(--ink); }
  .body-text + .body-text { margin-top: 4px; }
  .small-head { font-family: "Montserrat", Arial, sans-serif; font-size: 6px; font-weight: 600; color: var(--rose); letter-spacing: .5px; }

  /* Cover */
  .cover-photo { inset: 0; background:
      radial-gradient(ellipse 60px 90px at 232px 110px, #c9b7ad 0%, rgba(201,183,173,0) 100%),
      linear-gradient(100deg, #f1efed 0%, #e4dfdc 45%, #bfb2aa 72%, #958a84 100%); }
  .cover-brand { left: 22px; top: 100px; display: flex; align-items: center; gap: 6px; }
  .brand-dot { width: 10px; height: 10px; border-radius: 50%; background: var(--rose); }
  .brand-name { font-family: "Montserrat", Arial, sans-serif; font-size: 8px; font-weight: 600; letter-spacing: 1.4px; color: var(--charcoal); }

  /* Introduction */
  .intro-panel { left: 0; top: 0; width: 142px; height: 100%; background: var(--charcoal); }
  .intro-title { left: 14px; top: 14px; font-family: "Montserrat", Arial, sans-serif; font-size: 8px; letter-spacing: 1px; color: var(--paper); }
  .portrait { left: 156px; top: 12px; width: 22px; height: 22px; border-radius: 50%; background: linear-gradient(135deg, #c9b9b0, #8d7f78); }
  .person-name { left: 184px; top: 15px; font-size: 5px; font-weight: 600; color: var(--charcoal); }
  .person-role { left: 184px; top: 23px; font-size: 4.5px; color: var(--grey); }
  .rose-text { color: var(--rose); }

  /* Services photo slide */
  .team-photo { left: 16px; top: 32px; width: 138px; height: 80px; background:
      radial-gradient(circle at 50% 40%, #b49a8c 0%, rgba(180,154,140,0) 60%),
      linear-gradient(135deg, #d9d2ce, #6f6460); }
  .side-card { left: 162px; top: 32px; width: 132px; height: 80px; background: var(--grey-light); }

  /* Process grid */
  .icon-dot { width: 16px; height: 16px; border-radius: 50%; border: 1px solid var(--rose); display: flex; align-items: center; justify-content: center; }
  .rose-box { width: 64px; height: 36px; border-radius: 8px; background: var(--rose-soft); color: var(--paper); font-size: 4.6px; line-height: 1.5; padding: 6px; }
  .rose-box.strong { background: var(--rose); }
  .rose-box b { display: block; font-size: 5.5px; }

  /* Circles slide */
  .ring { width: 46px; height: 46px; border-radius: 50%; border: 1px solid var(--rose-soft); display: flex; align-items: center; justify-content: center; }

  /* Three services */
  .service-photo { top: 40px; width: 86px; height: 76px; }
  .service-tag { top: 118px; width: 86px; height: 11px; font-size: 5px; color: var(--paper); text-align: center; line-height: 11px; font-weight: 600; }

  /* Contact */
  .contact-photo { inset: 0; background:
      radial-gradient(ellipse 50px 80px at 150px 90px, #b8aaa2 0%, rgba(184,170,162,0) 100%),
      linear-gradient(110deg, #6f7d86 0%, #c4c4c6 38%, #ece8e5 62%, #bdb6b1 100%); }
  .contact-box { left: 176px; top: 96px; width: 112px; height: 84px; background: var(--rose-soft); }
  .contact-head { left: 176px; top: 96px; width: 112px; height: 22px; background: var(--rose); color: var(--paper); font-family: "Montserrat", Arial, sans-serif; font-size: 7px; letter-spacing: 1px; line-height: 22px; padding-left: 10px; }
</style>
</head>
<body>

<!-- Cover -->
<section class="slide col-left row-1">
  <div class="photo cover-photo" role="img" aria-label="Photo of a presenter in a light office gesturing toward the audience"></div>
  <div class="abs cover-brand"><span class="brand-dot"></span><span class="brand-name">VELVET HARBOR</span></div>
</section>

<!-- Introduction -->
<section class="slide col-right row-1">
  <div class="abs intro-panel"></div>
  <div class="abs intro-title">INTRODUCTION</div>
  <div class="photo portrait" role="img" aria-label="Small round portrait photo of the speaker"></div>
  <div class="abs person-name">Mara Ellis</div>
  <div class="abs person-role">Founder &amp; CEO</div>
  <div class="abs" style="left:156px; top:42px; width:140px;">
    <p class="body-text">We help small and medium businesses grow with thoughtful social media, clear digital strategy and content that feels personal, polished and true to the brand behind it.</p>
    <p class="body-text rose-text">Boutique care for every brand we touch, from the first post to the final report.</p>
    <p class="body-text">Our team plans, creates and manages your channels so you can stay focused on the work you love. Every campaign starts with listening and ends with results you can measure.</p>
    <p class="body-text">We keep our client list small on purpose, which means real attention, quick replies and ideas shaped around your goals.</p>
  </div>
</section>

<!-- Our Services (photo + text) -->
<section class="slide col-left row-2">
  <div class="slide-title left">OUR SERVICES</div>
  <div class="photo team-photo" role="img" aria-label="Photo of a team joining hands in a huddle"></div>
  <div class="abs side-card"></div>
  <div class="abs small-head" style="left:170px; top:40px;">LOREM IPSUM</div>
  <p class="abs body-text" style="left:170px; top:50px; width:118px;">Strategy, content and community built around your goals, with monthly planning and honest reporting on every channel we manage for you.</p>
  <div class="abs" style="left:16px; top:122px; width:278px;">
    <p class="body-text">From planning to reporting, we handle every detail so you can focus on running your business. We write the posts, design the visuals, schedule the calendar and answer your audience in a voice that sounds like you.</p>
    <p class="body-text">Monthly reviews keep results clear, and each quarter we refresh the plan so your brand keeps moving forward with purpose and style.</p>
  </div>
</section>

<!-- Process grid -->
<section class="slide col-right row-2">
  <div class="slide-title">LOREM IPSUM DOLOR SIT AMET</div>
  <div class="abs icon-dot" style="left:18px; top:44px;"><svg width="8" height="8" viewBox="0 0 8 8"><path d="M1 6 L3 4 L5 5 L7 2" stroke="#e8845f" fill="none"/></svg></div>
  <p class="abs body-text" style="left:40px; top:42px; width:92px;">Social media management across every key channel.</p>
  <div class="abs rose-box" style="left:140px; top:40px;"><b>Plan</b>Goals, audience and calendar.</div>
  <div class="abs rose-box strong" style="left:214px; top:40px;"><b>Create</b>Posts, visuals and copy.</div>

  <div class="abs icon-dot" style="left:18px; top:112px;"><svg width="8" height="8" viewBox="0 0 8 8"><path d="M1 4 L3 6 L7 1" stroke="#e8845f" fill="none"/></svg></div>
  <p class="abs body-text" style="left:40px; top:110px; width:92px;">Paid campaigns and clear monthly reporting.</p>
  <div class="abs rose-box" style="left:140px; top:108px;"><b>Grow</b>Ads that reach buyers.</div>
  <div class="abs rose-box strong" style="left:214px; top:108px;"><b>Measure</b>Results you can read.</div>
</section>

<!-- Three circles -->
<section class="slide col-left row-3">
  <div class="slide-title">LOREM IPSUM DOLOR SIT AMET</div>
  <div class="abs ring" style="left:100px; top:50px;"><svg width="18" height="18" viewBox="0 0 18 18"><rect x="3" y="3" width="12" height="12" rx="2" fill="#e8845f"/></svg></div>
  <div class="abs ring" style="left:160px; top:50px;"><svg width="18" height="18" viewBox="0 0 18 18"><path d="M2 16 V8 L6 10 V8 L10 10 V4 H14 V16 Z" fill="#e8845f"/></svg></div>
  <div class="abs ring" style="left:130px; top:100px;"><svg width="18" height="18" viewBox="0 0 18 18"><circle cx="9" cy="9" r="6" fill="#e8845f"/></svg></div>
  <p class="abs body-text" style="left:16px; top:58px; width:78px; text-align:right;">Brand strategy shaped to fit your market and the people you serve.</p>
  <p class="abs body-text" style="left:214px; top:58px; width:80px;">Local reach for growing businesses in every category.</p>
  <p class="abs body-text" style="left:184px; top:110px; width:100px;">Personal service from start to finish, with one team that knows you.</p>
</section>

<!-- Our Services (three) -->
<section class="slide col-right row-3">
  <div class="slide-title">OUR SERVICES</div>
  <div class="photo service-photo" style="left:16px; background:linear-gradient(135deg,#d5c3b8,#7d6d66);" role="img" aria-label="Photo of a smiling team member"></div>
  <div class="photo service-photo" style="left:112px; background:linear-gradient(135deg,#c9a890,#6e5a50);" role="img" aria-label="Photo of a colleague outdoors"></div>
  <div class="photo service-photo" style="left:208px; background:linear-gradient(135deg,#e0dedc,#8a8583);" role="img" aria-label="Photo of a professional in a bright office"></div>
  <div class="abs service-tag" style="left:16px; background:var(--rose);">Social</div>
  <div class="abs service-tag" style="left:112px; background:var(--grey);">Content</div>
  <div class="abs service-tag" style="left:208px; background:var(--grey);">Ads</div>
  <p class="abs body-text" style="left:16px; top:136px; width:86px;">Short posts that spark real conversation and build a loyal community.</p>
  <p class="abs body-text" style="left:112px; top:136px; width:86px;">Visuals and copy made for you, styled to match your brand.</p>
  <p class="abs body-text" style="left:208px; top:136px; width:86px;">Targeted ads that reach buyers and turn interest into sales.</p>
</section>

<!-- Collage -->
<section class="slide col-left row-4">
  <div class="slide-title">LOREM IPSUM DOLOR SIT AMET</div>
  <div class="photo" style="left:0; top:32px; width:100px; height:80px; background:linear-gradient(135deg,#b7c4cc,#5f6b73);" role="img" aria-label="Photo of colleagues meeting at a desk"></div>
  <div class="abs" style="left:104px; top:32px; width:100px; height:80px; background:var(--rose);"></div>
  <p class="abs body-text" style="left:112px; top:42px; width:84px; color:var(--paper);">Results you can see and share. We turn every campaign into clear numbers and simple next steps.</p>
  <div class="photo" style="left:208px; top:32px; width:102px; height:80px; background:linear-gradient(135deg,#e0dbd6,#8c8580);" role="img" aria-label="Photo of a hand holding a smartphone"></div>
  <div class="abs" style="left:0; top:116px; width:100px; height:101px; background:var(--grey);"></div>
  <p class="abs body-text" style="left:10px; top:130px; width:82px; color:var(--paper);">We listen first, then build a plan that fits your voice, budget and goals.</p>
  <div class="photo" style="left:104px; top:116px; width:100px; height:101px; background:linear-gradient(135deg,#a8b8c6,#56606a);" role="img" aria-label="Photo of a smiling group of professionals"></div>
  <div class="abs" style="left:208px; top:116px; width:102px; height:101px; background:var(--rose-soft);"></div>
  <p class="abs body-text" style="left:216px; top:130px; width:86px; color:var(--paper);">Clear plans, steady growth and a team that cares about your success.</p>
</section>

<!-- Contact -->
<section class="slide col-right row-4">
  <div class="photo contact-photo" role="img" aria-label="Photo of a client meeting across a table"></div>
  <div class="abs contact-box"></div>
  <div class="abs contact-head">CONTACT US</div>
  <div class="abs" style="left:186px; top:124px; width:96px; color:var(--paper);">
    <p class="body-text" style="color:var(--paper);">(555) 014-2290</p>
    <p class="body-text" style="color:var(--paper);">hello@velvetharbor.com</p>
    <p class="body-text" style="color:var(--paper);">velvetharbor.com</p>
  </div>
</section>

</body>
</html>
```